Helderveld.nu en Vemoran brochure

We offer the best supplements without unwanted additives and with a positive environment footprint. We have currently 2 brands. Helderveld.nu and Vemoran.
Helderveld.nu is a 100% plasticfree, vegan, non-gmo brand offering pure vegan casave capsules filled with active ingrediënts only.

Vemoran is also vegan, non-gmo and consists only of liquid formulas with liposomes. Garantee for the best absorption of nutrients into the cells

We need a beautifull brochure/catalog displaying our products, product info, brand info and key values. The final design should communicate health, nature and environment. It will be printed on agricultural waste instead of paper! Further reducing our carbon footprint.

Target Market(s)

Health and sport supplements in Europe, mainly the Netherlands, Belgium and Luxembourg

Industry/Entity Type

Supplement

Font styles to use
Sans Serif
Decorative

Requirements
Must have
• Nice pictures and product images.
clear titels.
Visually attractive.

- front and back cover
- about us page
- info page(s) about scientific proven concepts, health and enviorment
- product pages WITH BACKGROUND PICTURES association with the products (like sport, people, Nature, sources like the acacia tree etc.)
- pricing list with EAN codes and prices
Nice to have
• icons for glutenfree, sugarfree, vegan etc.
icons for use: gut health, brain health, sports/athletes, energy, recover etc.

2 brands in 1 catalog/brochure. Maybe you can make 2 sides. One for each brand.
The company (my company) is Helderveld.nu
The brands that i represent in the Netherlands & belgium are: Vemoran and Helderveld.nu

vemoran-drops.co.uk is NOT my website. I am in The Netherlandsm not UK.
Should not have
• Medical claims

```html
<!DOCTYPE html>
<html lang="nl">
<head>
<meta charset="utf-8">
<title>Helderveld.nu &amp; Vemoran – Catalogus 2021</title>
<link rel="stylesheet" href="https://fonts.googleapis.com/css2?family=Oswald:wght@500&family=Roboto+Condensed:wght@500&display=swap">
<style>
  :root {
    --leaf-green: #9bb72a;
    --leaf-green-dark: #8eaa22;
    --paper: #ffffff;
    --text-light: #ffffff;
    --gym-cool: #8f979c;
    --gym-warm: #c59a6e;
    --gym-shadow: #3b3e42;
    --kraft: #b48a5c;
    --pouch-label: #eeeeec;
    --bottle-amber: #4a1f1c;
    --cap: #f1f1f1;
  }
  html, body {
    margin: 0;
    padding: 0;
    width: 1200px;
    height: 863px;
    overflow: hidden;
    background: var(--paper);
  }
  .cover {
    position: relative;
    width: 1200px;
    height: 863px;
    background: var(--leaf-green);
    overflow: hidden;
  }
  .cover__band-top {
    position: absolute;
    inset: 0 0 auto 0;
    height: 147px;
    background: var(--leaf-green);
    border-bottom: 2px solid var(--leaf-green-dark);
  }
  .cover__tagline {
    position: absolute;
    right: 128px;
    top: 109px;
    margin: 0;
    font-family: "Roboto Condensed", sans-serif;
    font-weight: 500;
    font-size: 20px;
    letter-spacing: 0.42em;
    color: var(--text-light);
    line-height: 1;
  }
  .cover__photo {
    position: absolute;
    left: 0;
    top: 149px;
    width: 1200px;
    height: 441px;
    background:
      linear-gradient(180deg, rgba(255,255,255,0.15) 0%, rgba(0,0,0,0) 30%, rgba(0,0,0,0.25) 100%),
      linear-gradient(90deg, var(--gym-warm) 0%, var(--gym-cool) 35%, var(--gym-shadow) 60%, var(--gym-cool) 85%, #b9c1c4 100%);
  }
  .cover__products-pouch {
    position: absolute;
    left: 104px;
    top: 303px;
    width: 239px;
    height: 428px;
    border-radius: 6px 6px 4px 4px;
    background: linear-gradient(180deg, var(--kraft) 0%, var(--kraft) 27%, var(--pouch-label) 27%, var(--pouch-label) 100%);
    box-shadow: 0 10px 18px rgba(0,0,0,0.2);
  }
  .cover__products-bottle {
    position: absolute;
    left: 292px;
    top: 438px;
    width: 135px;
    height: 313px;
    border-radius: 24px 24px 14px 14px;
    background: linear-gradient(180deg, var(--cap) 0%, var(--cap) 13%, var(--bottle-amber) 13%, #2c1210 100%);
    box-shadow: 0 10px 18px rgba(0,0,0,0.25);
  }
  .cover__title {
    position: absolute;
    right: 134px;
    top: 599px;
    margin: 0;
    font-family: "Oswald", sans-serif;
    font-weight: 500;
    color: var(--text-light);
    text-align: right;
    line-height: 1;
  }
  .cover__title-word {
    display: block;
    font-size: 72px;
    letter-spacing: 0.01em;
  }
  .cover__title-year {
    display: block;
    margin-top: 3px;
    font-size: 64px;
    letter-spacing: 0.01em;
  }
</style>
</head>
<body>
  <main class="cover">
    <div class="cover__band-top">
      <p class="cover__tagline">POWER OF NATURE</p>
    </div>

    <div class="cover__photo" role="img" aria-label="Photo of people running on treadmills in a bright gym with large windows"></div>

    <div class="cover__products-pouch" role="img" aria-label="Product photo of a Helderveld.nu kraft paper supplement pouch with two white capsules"></div>
    <div class="cover__products-bottle" role="img" aria-label="Product photo of a Vemoran liposomal multivitamin bottle, 250 ml"></div>

    <h1 class="cover__title">
      <span class="cover__title-word">CATALOGUS</span>
      <span class="cover__title-year">2021</span>
    </h1>
  </main>
</body>
</html>
```